Label design for Bloody Mary mix

we are looking for a label design for a Bloody Mary mix we are making. we are calling it "Rusty Gatepost"
thinking of maybe a farm girl pin up with a tattoo??
Open to all ideas
Thanks for your help!!!

Target Market(s)

Bloody Mary drinkers :)

Industry/Entity Type

Farm

Font styles to use
Serif
Sans Serif
Decorative
Script
Other font styles liked:
• any

Colors

Designer to choose colors to be used in the design.

```html
<!DOCTYPE html>
<html lang="en">
<head>
<meta charset="utf-8">
<title>Rusty Gatepost – Premium Bloody Mary Mixxx Labels</title>
<link rel="stylesheet" href="https://fonts.googleapis.com/css2?family=Montserrat:wght@400;500;700;800&display=swap">
<style>
  :root {
    --page: #ffffff;
    --ink: #111111;
    --red: #e3141b;
    --red-deep: #b50008;
    --red-bright: #ff1a1a;
    --silver-light: #f0f0f0;
    --silver-mid: #bdbdbd;
    --silver-dark: #7d7d7d;
    --white: #ffffff;
    --art-dark: #2a2a2a;
    --art-grey: #8a8a8a;
  }
  * { box-sizing: border-box; margin: 0; padding: 0; }
  html, body {
    width: 1200px; height: 999px; overflow: hidden;
    background: var(--page);
    font-family: "Montserrat", Arial, sans-serif;
  }
  .canvas { position: relative; width: 1200px; height: 999px; }

  .label {
    position: absolute; top: 378px;
    width: 358px; height: 412px;
  }
  .label--silver { left: 181px; }
  .label--red { left: 670px; }

  .label__shape { position: absolute; inset: 0; width: 100%; height: 100%; }

  .label__tagline {
    position: absolute; top: 25px; left: 0; right: 0;
    text-align: center; font-size: 11.5px; font-weight: 500;
    letter-spacing: 1.6px; color: var(--red);
  }
  .label--red .label__tagline { color: var(--white); }

  .label__art {
    position: absolute; top: 62px; left: 58px;
    width: 250px; height: 134px;
    border-radius: 70px 70px 10px 10px;
    background:
      radial-gradient(ellipse at 48% 32%, var(--art-dark) 0 34%, transparent 35%),
      linear-gradient(180deg, var(--art-grey) 0%, var(--art-dark) 100%);
    opacity: .9;
  }

  .label__brand {
    position: absolute; top: 212px; left: 0; right: 0;
    text-align: center; color: var(--red);
    font-weight: 800; font-size: 44px; line-height: 1.02;
    letter-spacing: -.5px;
  }
  .label--red .label__brand { color: var(--white); }

  .label__product {
    position: absolute; top: 342px; left: 0; right: 0;
    text-align: center; font-size: 14.5px; font-weight: 400;
    letter-spacing: .6px; color: var(--ink);
  }
  .label__product strong { font-weight: 700; color: var(--red); letter-spacing: .3px; }
  .label--red .label__product strong { color: var(--white); }
  .label__product .mixxx { letter-spacing: 3px; }

  .label__volume {
    position: absolute; top: 378px; left: 0; right: 0;
    text-align: center; font-size: 7px; font-weight: 500; color: var(--ink);
  }
</style>
</head>
<body>
<main class="canvas">

  <section class="label label--silver">
    <svg class="label__shape" viewBox="0 0 358 412" aria-hidden="true">
      <defs>
        <linearGradient id="silver" x1="0" x2="1" y1="0" y2="0">
          <stop offset="0" stop-color="#bdbdbd"/>
          <stop offset=".35" stop-color="#f0f0f0"/>
          <stop offset=".7" stop-color="#bdbdbd"/>
          <stop offset="1" stop-color="#7d7d7d"/>
        </linearGradient>
      </defs>
      <path d="M0 26 Q179 -22 358 26 L358 384 Q179 432 0 384 Z" fill="url(#silver)"/>
      <path d="M8 33 Q179 -10 350 33 L350 377 Q179 420 8 377 Z" fill="none" stroke="#e3141b" stroke-width="1"/>
    </svg>
    <p class="label__tagline">PREMUIM QUALITY</p>
    <div class="label__art" role="img" aria-label="Illustration of a farm girl in a wide hat holding a tomato, with barn, tractor and fields behind"></div>
    <h1 class="label__brand">Rusty<br>Gatepost</h1>
    <p class="label__product">PREMIUM <strong>BLOODY MARY</strong> <span class="mixxx">MIXXX</span></p>
    <p class="label__volume">32 fl OZ (1 Quart) 946 mL</p>
  </section>

  <section class="label label--red">
    <svg class="label__shape" viewBox="0 0 358 412" aria-hidden="true">
      <defs>
        <linearGradient id="redfoil" x1="0" x2="1" y1="0" y2="0">
          <stop offset="0" stop-color="#b50008"/>
          <stop offset=".4" stop-color="#ff1a1a"/>
          <stop offset=".75" stop-color="#e3141b"/>
          <stop offset="1" stop-color="#b50008"/>
        </linearGradient>
      </defs>
      <path d="M0 26 Q179 -22 358 26 L358 384 Q179 432 0 384 Z" fill="url(#redfoil)"/>
      <path d="M8 33 Q179 -10 350 33 L350 377 Q179 420 8 377 Z" fill="none" stroke="#b50008" stroke-width="1"/>
    </svg>
    <p class="label__tagline">PREMUIM QUALITY</p>
    <div class="label__art" role="img" aria-label="Illustration of a farm girl in a wide hat holding a tomato, with barn, tractor and fields behind"></div>
    <h1 class="label__brand">Rusty<br>Gatepost</h1>
    <p class="label__product">PREMIUM <strong>BLOODY MARY</strong> <span class="mixxx">MIXXX</span></p>
    <p class="label__volume">32 fl OZ (1 Quart) 946 mL</p>
  </section>

</main>
</body>
</html>
```